Homepage and Interior Page Design for BrontaLux

We will provide all logos, graphics and images as well as a wireframe of the desired homepage layout. Deliverables should be two well formated Photoshop files will well named layers, one for the homepage and one for an interior page. The "Puzzle Animation" will be developed separately. This will be a puzzle that breaks apart and reassembles to rotate the images. Here is the old site: https://www.brontalux.example/

Target Market(s)

Small to mid sized manufacturers.

Number of Pages Required

2 page

Font styles to use
Sans Serif

Colors

Designer to choose colors to be used in the design.

Requirements
Must have
• 2 layered photoshop files ready for slicing to HTML will well labeled layers
Nice to have
• If you are interested in creating the animation as a separate project, let me know.

```html
<!DOCTYPE html>
<html lang="en">
<head>
<meta charset="utf-8">
<title>BrontaLux – Homepage</title>
<link href="https://fonts.googleapis.com/css2?family=Montserrat:wght@300;400;500;600;700&family=Libre+Baskerville&family=Italianno&display=swap" rel="stylesheet">
<style>
  :root{
    --stage:#a9aab4;
    --bar:#1b1c2a;
    --nav:#2a2c3e;
    --ink:#15161f;
    --cyan:#19b7cf;
    --red:#e1261c;
    --white:#ffffff;
    --muted:#7d8093;
    --card:#1d2030;
    --footer:#050506;
  }
  *{box-sizing:border-box;margin:0;padding:0}
  html,body{width:786px;height:1200px;overflow:hidden}
  body{background:var(--stage);font-family:'Montserrat',sans-serif;position:relative}
  .page{position:absolute;left:5px;top:0;width:776px;height:1200px;background:var(--bar);overflow:hidden}
  .abs{position:absolute}

  /* top bar */
  .topbar{left:0;top:0;width:776px;height:43px;background:var(--bar)}
  .contact{left:146px;top:16px;font-size:6px;letter-spacing:1px;color:var(--cyan);display:flex;align-items:center;gap:12px}
  .contact .label{color:var(--muted)}
  .social-top{left:515px;top:15px;display:flex;align-items:center;gap:14px;font-size:6px;color:var(--muted)}
  .dot{width:7px;height:7px;border-radius:50%;background:var(--white);display:inline-block}
  .logo-box{left:332px;top:0;width:111px;height:53px;background:var(--white);border:3px solid var(--cyan);display:flex;align-items:center;justify-content:center;z-index:3}
  .logo-box span{font-weight:600;font-size:14px;color:#1d7fc4}

  /* nav */
  .nav{left:0;top:43px;width:776px;height:37px;background:var(--nav);display:flex;justify-content:center;align-items:flex-end;padding-bottom:10px;gap:22px;font-size:5.5px;font-weight:600;color:var(--white);letter-spacing:.3px}
  .nav .active{color:var(--cyan)}

  /* hero */
  .hero{left:0;top:80px;width:776px;height:325px;background:radial-gradient(circle at 62% 62%,#ffe2b0 0,#4ea3ff 9%,#154fb8 30%,#0b2a6e 60%,#07122e 100%)}
  .hero svg{position:absolute;left:0;top:0}
  .hero-copy{left:146px;top:54px}
  .hero-copy h1{font-size:11.5px;font-weight:700;letter-spacing:2px;line-height:18px;color:var(--ink)}
  .hero-copy p{font-size:4.8px;font-weight:600;letter-spacing:1.5px;color:var(--ink);margin-top:3px}
  .btn-red{display:inline-block;margin-top:12px;width:69px;height:20px;background:var(--red);color:var(--white);font-size:4.8px;font-weight:700;letter-spacing:1.2px;line-height:20px;text-align:center}

  /* experience */
  .experience{left:0;top:405px;width:776px;height:226px;background:var(--bar)}
  .exp-label{left:146px;top:87px;font-size:4.8px;font-weight:600;letter-spacing:1.4px;color:var(--white)}
  .exp-title{left:146px;top:97px;font-family:'Libre Baskerville',serif;font-size:12px;line-height:16px;letter-spacing:2px;color:var(--cyan)}
  .exp-text{left:146px;top:134px;width:160px;font-size:5px;line-height:9px;color:var(--muted)}
  .big-num{left:386px;top:12px;font-family:'Italianno',cursive;font-size:170px;line-height:1;color:#3a3d52}
  .years{left:535px;top:107px;font-size:20px;font-weight:300;letter-spacing:1px;color:#c9cbd6}
  .years small{display:block;font-size:5.5px;letter-spacing:1.6px;color:var(--muted);margin-top:-1px}

  /* services */
  .services{left:0;top:631px;width:776px;height:363px;background:linear-gradient(180deg,#2b2d38 0,#3b3e4a 45%,#30323c 100%)}
  .cards{left:146px;top:52px;width:485px;display:flex}
  .card{width:121.25px;height:272px;background:var(--card);border-top:12px solid var(--cyan);text-align:center;padding:0 13px}
  .card .photo{height:103px;margin-top:0;border:1px solid #3c4052}
  .card h3{font-family:'Libre Baskerville',serif;font-weight:400;font-size:10px;line-height:12px;letter-spacing:1.5px;color:var(--cyan);height:52px;display:flex;align-items:center;justify-content:center;margin-top:8px}
  .card p{font-size:4.5px;line-height:9.5px;color:#a6a9b8}
  .card .btn{display:inline-block;margin-top:20px;width:72px;height:14px;line-height:14px;background:var(--cyan);color:var(--white);font-size:4.5px;font-weight:700;letter-spacing:1px}

  /* footer */
  .footer{left:0;top:994px;width:776px;height:206px;background:var(--footer);text-align:center}
  .footer-logo{left:0;top:28px;width:776px;font-weight:600;font-size:15px;color:var(--white)}
  .footer-rule{left:358px;top:49px;width:60px;height:1px;background:var(--white)}
  .footer-text{left:218px;top:74px;width:340px;font-size:4.8px;line-height:10px;color:#3e404c}
  .footer-social{left:0;top:122px;width:776px;display:flex;justify-content:center;gap:38px}
  .footer-social .dot{width:6px;height:6px}
  .footer-links{left:0;top:150px;width:776px;display:flex;justify-content:center;gap:14px;font-size:4.2px;font-weight:500;color:#c9cbd6;letter-spacing:.3px}
  .copyright{left:0;top:184px;width:776px;font-size:4.2px;color:#4c4e5a}
</style>
</head>
<body>
<div class="page">

  <header class="abs topbar">
    <div class="abs contact">
      <svg width="7" height="7" viewBox="0 0 24 24"><path fill="#ffffff" d="M6.6 10.8a15.1 15.1 0 0 0 6.6 6.6l2.2-2.2c.3-.3.7-.4 1-.2 1.1.4 2.3.6 3.6.6.6 0 1 .4 1 1V20c0 .6-.4 1-1 1A17 17 0 0 1 3 4c0-.6.4-1 1-1h3.5c.6 0 1 .4 1 1 0 1.3.2 2.5.6 3.6.1.3 0 .7-.2 1z"/></svg>
      <span>555 014 2290</span><span class="label">call us</span>
    </div>
    <div class="abs social-top"><span>touch with us</span><span class="dot"></span><span class="dot"></span><span class="dot"></span></div>
  </header>

  <div class="abs logo-box"><span>BrontaLux</span></div>

  <nav class="abs nav">
    <span class="active">CONTRACT PACKAGING</span>
    <span>PRODUCT ASSEMBLY</span>
    <span>CUSTOM PALLETS &amp; CRATES</span>
    <span>INVENTORY MANAGEMENT &amp; FULFILLMENT</span>
    <span>ABOUT</span>
    <span>CONTACT</span>
  </nav>

  <section class="abs hero" role="img" aria-label="Welder at work with bright sparks in blue light, split into a puzzle grid">
    <svg width="776" height="325" viewBox="0 0 776 325">
      <g stroke="#ffffff" stroke-opacity=".8" stroke-width="1">
        <line x1="322" y1="0" x2="322" y2="325"/><line x1="388" y1="0" x2="388" y2="325"/>
        <line x1="453" y1="0" x2="453" y2="325"/><line x1="518" y1="0" x2="518" y2="325"/>
        <line x1="583" y1="0" x2="583" y2="325"/><line x1="648" y1="0" x2="648" y2="325"/>
        <line x1="713" y1="0" x2="713" y2="325"/>
        <line x1="62" y1="263" x2="62" y2="325"/><line x1="127" y1="263" x2="127" y2="325"/>
        <line x1="192" y1="182" x2="192" y2="325"/><line x1="257" y1="182" x2="257" y2="325"/>
        <line x1="322" y1="64" x2="776" y2="64"/><line x1="322" y1="129" x2="776" y2="129"/>
        <line x1="192" y1="194" x2="776" y2="194"/><line x1="0" y1="263" x2="776" y2="263"/>
      </g>
      <g fill="#ffffff">
        <rect x="0" y="0" width="322" height="182"/>
        <rect x="0" y="182" width="193" height="81"/>
        <rect x="583" y="64" width="65" height="65"/>
        <rect x="648" y="129" width="65" height="65"/>
        <rect x="453" y="194" width="65" height="65"/>
        <rect x="322" y="260" width="66" height="65"/>
      </g>
    </svg>
    <div class="abs hero-copy">
      <h1>PACKAGING AND<br>ASSEMBLY EXPERTS</h1>
      <p>LOREM IPSUM DOLOR SIT AMET</p>
      <a class="btn-red">KNOW MORE</a>
    </div>
  </section>

  <section class="abs experience">
    <div class="abs big-num">36</div>
    <div class="abs exp-label">LOREM IPSUM DOLOR SIT AMET</div>
    <h2 class="abs exp-title">SECRET OF<br>SUCCESS</h2>
    <p class="abs exp-text">Lorem ipsum dolor sit amet, consectetur adipiscing elit, sed do eiusmod tempor incididunt ut labore et dolore magna aliqua. Ut enim ad minim veniam.</p>
    <div class="abs years">YEARS<small>OF EXPERIENCE</small></div>
  </section>

  <section class="abs services" role="img" aria-label="Blurred warehouse interior with loading doors">
    <div class="abs cards">
      <article class="card">
        <div class="photo" role="img" aria-label="Workers packing boxes at a table" style="background:linear-gradient(160deg,#c9a27a,#7a5a44 60%,#3b3532)"></div>
        <h3>CONTRACT<br>PACKAGING</h3>
        <p>We cover the spectrum of visible retail packaging, from blisters to clamshells to stretchpak</p>
        <a class="btn">KNOW MORE</a>
      </article>
      <article class="card">
        <div class="photo" role="img" aria-label="Hands assembling small metal parts" style="background:linear-gradient(160deg,#c7ccd4,#8b919c 55%,#4a4f5a)"></div>
        <h3>PRODUCT<br>ASSEMBLY</h3>
        <p>We cover the spectrum of visible retail packaging, from blisters to clamshells to stretchpak</p>
        <a class="btn">KNOW MORE</a>
      </article>
      <article class="card">
        <div class="photo" role="img" aria-label="Wooden crates stacked in a container" style="background:linear-gradient(180deg,#3a2a1e,#a0703f 45%,#6b4a2c)"></div>
        <h3>CUSTOM<br>PALLETS &amp;<br>CRATES</h3>
        <p>We cover the spectrum of visible retail packaging, from blisters to clamshells to stretchpak</p>
        <a class="btn">KNOW MORE</a>
      </article>
      <article class="card">
        <div class="photo" role="img" aria-label="Warehouse aisle with tall shelving" style="background:linear-gradient(180deg,#2c4a6b,#8a6a4a 55%,#b85a30)"></div>
        <h3>INVENTORY<br>MANAGEMENT<br>&amp; FULFILLMENT</h3>
        <p>We cover the spectrum of visible retail packaging, from blisters to clamshells to stretchpak</p>
        <a class="btn">KNOW MORE</a>
      </article>
    </div>
  </section>

  <footer class="abs footer">
    <div class="abs footer-logo">BrontaLux</div>
    <div class="abs footer-rule"></div>
    <p class="abs footer-text">Lorem ipsum dolor sit amet, consectetur adipiscing elit, sed do eiusmod tempor incididunt ut labore et dolore magna aliqua. Ut enim ad minim veniam, quis nostrud exercitation ullamco laboris nisi ut aliquip ex ea commodo consequat.</p>
    <div class="abs footer-social"><span class="dot"></span><span class="dot"></span><span class="dot"></span><span class="dot"></span></div>
    <div class="abs footer-links">
      <span>HOME</span><span>CONTRACT PACKAGING</span><span>INVENTORY MANAGEMENT &amp; FULFILLMENT</span><span>PRODUCT ASSEMBLY</span><span>CUSTOM PALLETS &amp; CRATES</span><span>ABOUT US</span><span>CONTACT US</span><span>SITE MAP</span>
    </div>
    <div class="abs copyright">© 2018 BrontaLux Ltd. All Rights Reserved</div>
  </footer>

</div>
</body>
</html>
```